Fatigued and Overloaded by COVID Messages? We need original illustrations to show that.

Everywhere you look there are messages about COVID. That is leading many people to feel fatigued and overloaded by the messages.

We surveyed U.S. adults March 20th - 24th, 2020 and measured message fatigue, information overload, perceived repetition, and perceived exaggeration. Here is how participants responded:

When it comes to coronavirus . . .
55% feel exhausted by all the messages.
54% feel overloaded by the amount of information.
51% feel that the messages are repetitive.
47% feel like messages exaggerate how bad it is.

In other words, almost half of U.S. adults show signs of message fatigue, information overload, perceived message repetition, and perceived message exaggeration.

We will continue to survey 400 adults every week for the next 16 weeks. Each time we will measure message fatigue, information overload, perceived repetition, and perceived exaggeration. We expect that it will increase over time.

What are we looking for? We need innovative and original illustrations that attempt to communicate these findings. The illustrations would visualize message fatigue, information overload, perceived message repetition, and perceived message exaggeration.

What sort of visual are we looking for? Our preference is for an original illustration (or set of illustrations). Our preference is for creative and powerful illustrations, but we are also open to the creative and well-executed infographics.

We need these images fast . We will award monetary prizes to the 3 best designs. If we like more than that, then we might purchase more (e.g., in past contests, we have purchased as many as 30 designs).

What we will need:
(1) The illustrations must be original and we will need the photoshop and/or illustrator files for all artwork. (By original, we mean that the illustrations are 100% created by you. Our organization requires that we utilize only original illustrated work. We have had issues with free imagery being pirated and reposted as free. We sidestep that issue by just having everything created.)

(2) The illustration should say, somewhere: "Based on a survey of 400 U.S. adults conducted March 20 - 24th, 2020."

(3) We will have almost 4 months worth of data by the time this is done. In other words, the illustrations might be able to help us present that weekly data.

(4) We have conducted other Artvendo projects. It might be helpful to examine designs we liked in the past. For example, here is another COVID project we just finished:

https://jobs.artvendo-example.com/job/5162048

Target Market(s)

U.S. adults

Requirements
Must have
• Original illustrations. Mobile friendly design. People will view this on their smartphones.
Nice to have
• A design that we can use to communicate the data across time.

```html
<!DOCTYPE html>
<html lang="en">
<head>
<meta charset="utf-8">
<title>Overloaded with COVID-19 News</title>
<link rel="stylesheet" href="https://fonts.googleapis.com/css2?family=Didact+Gothic&display=swap">
<style>
  :root {
    --page: #ffffff;
    --card: #b35c7e;
    --headline-blue: #3fb3ef;
    --arrow-grey: #a3b3bd;
    --panel: #c3c8d2;
    --panel-strip: #ececf0;
    --ink: #2b1a25;
    --bar: #34a8e0;
    --axis: #4a4a52;
    --figure-warm: #d9755a;
    --figure-cool: #5a6a8a;
  }
  html, body {
    margin: 0;
    width: 1200px;
    height: 1200px;
    overflow: hidden;
    background: var(--page);
  }
  .stage {
    position: relative;
    width: 1000px;
    height: 1000px;
    transform: scale(1.2);
    transform-origin: 0 0;
    font-family: "Didact Gothic", "Century Gothic", sans-serif;
    color: var(--ink);
  }
  .card {
    position: absolute;
    left: 152px; top: 30px;
    width: 696px; height: 940px;
    background: var(--card);
    border-radius: 16px;
  }
  .headline-art {
    position: absolute;
    left: 170px; top: 55px;
    width: 330px; height: 285px;
    border-radius: 40px;
    background: radial-gradient(ellipse at center, rgba(63,179,239,0.75), rgba(63,179,239,0.25) 70%, rgba(63,179,239,0) 100%);
  }
  .figure-art {
    position: absolute;
    left: 160px; top: 295px;
    width: 165px; height: 185px;
    border-radius: 30px;
    background: linear-gradient(180deg, var(--figure-warm) 0%, #e6c3a8 35%, var(--figure-cool) 60%, #7fa7b4 85%, var(--figure-warm) 100%);
    opacity: 0.85;
  }
  .pointer-arrow {
    position: absolute;
    left: 480px; top: 210px;
    width: 150px; height: 140px;
    overflow: visible;
  }
  .stats-panel {
    position: absolute;
    left: 330px; top: 362px;
    width: 490px; height: 215px;
    background: linear-gradient(90deg, var(--panel-strip) 0 68px, var(--panel) 68px);
    border-bottom-left-radius: 26px;
    box-shadow: 3px 4px 6px rgba(0,0,0,0.35);
  }
  .stat {
    position: absolute;
    margin: 0;
    font-size: 22px;
    line-height: 31px;
    text-shadow: 2px 2px 3px rgba(0,0,0,0.35);
  }
  .stat .value { position: absolute; left: 3px; top: 0; }
  .stat .label { position: absolute; left: 70px; top: 0; width: 410px; }
  .stat-exhausted  { top: 14px; left: 0; width: 490px; }
  .stat-overloaded { top: 45px; left: 0; width: 490px; }
  .stat-repetitive { top: 108px; left: 0; width: 490px; }
  .stat-exaggerate { top: 142px; left: 0; width: 490px; }
  .stat-overloaded .value { left: 0; }
  .stat-overloaded .label { left: 80px; }
  .stat-repetitive .value { left: 12px; }
  .stat-repetitive .label { left: 80px; }
  .stat-exaggerate .value { left: 6px; }
  .stat-exaggerate .label { left: 80px; }
  .chart-title {
    position: absolute;
    left: 222px; top: 608px;
    margin: 0;
    font-size: 21px;
    color: var(--ink);
  }
  .weekly-chart {
    position: absolute;
    left: 0; top: 0;
    width: 1000px; height: 1000px;
  }
  .weekly-chart text {
    font-family: "Didact Gothic", "Century Gothic", sans-serif;
    fill: var(--ink);
  }
  .axis-label { font-size: 17px; }
  .week-label { font-size: 14px; font-weight: bold; }
  .unit-label { font-size: 19px; font-weight: bold; }
  .source-note {
    position: absolute;
    left: 253px; top: 892px;
    margin: 0;
    font-size: 22px;
    line-height: 32px;
    color: var(--ink);
  }
</style>
</head>
<body>
<div class="stage">
  <div class="card"></div>

  <div class="headline-art" role="img" aria-label="Hand-lettered warped headline reading: overloaded with COVID 19 news"></div>
  <div class="figure-art" role="img" aria-label="Cartoon of a worried man bent over, straining under the weight of the headline"></div>

  <svg class="pointer-arrow" viewBox="0 0 150 140" aria-hidden="true">
    <path d="M10 30 C 55 10, 95 25, 110 75 L 128 70 L 100 130 L 62 82 L 82 82 C 72 55, 45 40, 10 30 Z"
          fill="var(--arrow-grey)" style="filter: drop-shadow(3px 3px 3px rgba(0,0,0,0.3));"/>
  </svg>

  <section class="stats-panel">
    <p class="stat stat-exhausted"><span class="value">55%</span><span class="label">feel exhausted by all the messages.</span></p>
    <p class="stat stat-overloaded"><span class="value">54%</span><span class="label">feel overloaded by the amount of information.</span></p>
    <p class="stat stat-repetitive"><span class="value">51%</span><span class="label">feel that the messages are repetitive</span></p>
    <p class="stat stat-exaggerate"><span class="value">47%</span><span class="label">feel like messages exaggerate how bad it is</span></p>
  </section>

  <p class="chart-title">% of people</p>

  <svg class="weekly-chart" viewBox="0 0 1000 1000" aria-label="Weekly percentage chart, weeks 1 to 16">
    <rect x="233" y="650" width="539" height="215" fill="var(--panel)"/>
    <path d="M233 665 Q233 650 248 650 L285 650 L285 865 L233 865 Z" fill="var(--panel-strip)"/>
    <line x1="285" y1="650" x2="285" y2="839" stroke="var(--axis)" stroke-width="5"/>
    <line x1="283" y1="838" x2="700" y2="838" stroke="var(--axis)" stroke-width="5"/>

    <text class="axis-label" x="244" y="683">100</text>
    <text class="axis-label" x="244" y="715">80</text>
    <text class="axis-label" x="244" y="747">60</text>
    <text class="axis-label" x="244" y="779">40</text>
    <text class="axis-label" x="244" y="811">20</text>
    <text class="axis-label" x="244" y="844">0</text>

    <rect x="296" y="745" width="11" height="91" fill="var(--bar)" stroke="#1d5f86" stroke-width="1"/>
    <rect x="315" y="747" width="11" height="89" fill="var(--bar)" stroke="#1d5f86" stroke-width="1"/>

    <g class="week-label" text-anchor="middle">
      <text x="298" y="858">1</text><text x="318" y="858">2</text><text x="340" y="858">3</text>
      <text x="362" y="858">4</text><text x="383" y="858">5</text><text x="404" y="858">6</text>
      <text x="425" y="858">7</text><text x="447" y="858">8</text><text x="468" y="858">9</text>
      <text x="494" y="858">10</text><text x="525" y="858">11</text><text x="557" y="858">12</text>
      <text x="590" y="858">13</text><text x="622" y="858">14</text><text x="654" y="858">15</text>
      <text x="686" y="858">16</text>
    </g>
    <text class="unit-label" x="717" y="858">week</text>
  </svg>

  <p class="source-note">Based on a survey of 400 U.S. adults conducted<br>March 20 - 24th, 2020</p>
</div>
</body>
</html>
```